Marine Business Card

We install Lighting, Sound, Video, PA Systems to hotels, nightclubs, Restaurants, Cruise Ships.

Target Market(s)

We want to focus on the Marine or Maritime/Cruise industry. Passenger ships and cruise liners are the companies we want to appeal to

Industry/Entity Type

Business

Contact Information for Business Card

Mark Tilbury
Managing Director
Harbourne Vista Audio Marine Ltd

Requirements
Must have
• Office: 01632 960482
Mobile: 07700 900317
mark@harbournevistaaudio.co.uk
www.harbournevistaaudio.co.uk

```html
<!DOCTYPE html>
<html lang="en">
<head>
<meta charset="utf-8">
<title>Harbourne Vista Audio Marine Ltd — Business Card</title>
<link rel="stylesheet" href="https://fonts.googleapis.com/css2?family=Crimson+Text&display=swap">
<style>
  :root {
    --page-bg: #ffffff;
    --card-bg: #231f20;
    --gold-text: #f6d27a;
    --gold-dark: #8c5b1d;
    --gold-light: #f3d895;
    --ink-light: #ffffff;
  }
  html, body {
    margin: 0;
    padding: 0;
    width: 1200px;
    height: 1000px;
    overflow: hidden;
    background: var(--page-bg);
  }
  .canvas {
    position: relative;
    width: 1200px;
    height: 1000px;
  }
  .card {
    position: absolute;
    left: 75px;
    top: 157px;
    width: 1035px;
    height: 680px;
    background: var(--card-bg);
  }
  .card-rule {
    position: absolute;
    height: 3px;
    background: linear-gradient(to right,
      transparent 0%,
      var(--gold-dark) 15%,
      var(--gold-light) 50%,
      var(--gold-dark) 85%,
      transparent 100%);
  }
  .card-rule.top { left: 240px; width: 738px; top: 244px; }
  .card-rule.bottom { left: 368px; width: 480px; top: 751px; }
  .contact {
    position: absolute;
    left: 75px;
    top: 392px;
    width: 1098px;
    text-align: center;
    font-family: "Crimson Text", "Goudy Old Style", Georgia, serif;
    font-variant-numeric: lining-nums;
  }
  .contact p { margin: 0; }
  .contact .phone {
    color: var(--gold-text);
    font-size: 47px;
    line-height: 55px;
  }
  .contact .web {
    color: var(--ink-light);
    font-size: 36px;
    line-height: 50px;
  }
  .contact .email { margin-top: 2px; }
</style>
</head>
<body>
<div class="canvas">
  <div class="card"></div>
  <div class="card-rule top"></div>
  <div class="card-rule bottom"></div>

  <div class="contact">
    <p class="phone">Office: 01632 960482</p>
    <p class="phone">Mobile: 07700 900317</p>
    <p class="web email">mark@harbournevistaaudio.co.uk</p>
    <p class="web site">www.harbournevistaaudio.co.uk</p>
  </div>
</div>
</body>
</html>
```